A WEBSITE FOR A JEWELLERY RETAIL STORE WITH A SHOPPING CART, AND ABILITY TO ORDER ONLINE.

I require a website with a shopping cart.

We sell MAINLY diamond jewellery (such as rings etc). I need it to be simple to change prices with only a few buttons, as the price fluctuates due to the US Dollar.

We are a diamond wholesaler, selling directly to the public, so we guarantee the lowest prices in Australia.

There is also a link to current inventory that will need to be uploaded to the site.

This could be an ongoing job, where you will be paid weekly to maintain and update the website if you wish.

Target Market(s)

People getting engaged, and wanting to buy a diamond ring.

Number of Pages Required

5+ page

Colors

Designer to choose colors to be used in the design.

Requirements
Must have
• elegant.
• modern.
• professional.
• SHOPPING CART.
• ABILITY TO SEARCH FOR LOOSE DIAMONDS (LINK THAT NEEDS TO BE EMBEDDED WILL BE SENT WHICH SHOWS CURRENT STOCK).
• ENGAGEMENT RINGS
• WEDDING RINGS
• DIAMOND EARRINGS
• DIAMOND PENDANTS
• LOOSE DIAMONDS.
• SALE ITEMS.
• OTHER JEWELLERY.
• EDUCATION
• WISH LIST
• CART.
Nice to have
• a good place to look for inspiration on pages is https://www.lumenvael.example.
• YOU MAY VISIT OUR FACEBOOK PAGE AT.
• HTTP://WWW.SOCIALPAGE.EXAMPLE/QUILLSTONEJEWELLERS
Should not have
• We don't want it too busy.

```html
<!DOCTYPE html>
<html lang="en">
<head>
<meta charset="utf-8">
<title>Quillstone Jewellers – 18K Yellow Gold Serelle</title>
<link href="https://fonts.googleapis.com/css2?family=Cormorant+Garamond:wght@400;500&family=Lato:wght@400&display=swap" rel="stylesheet">
<style>
:root{
  --ink:#111;
  --text:#222;
  --accent:#e8212b;
  --panel:#2a2a2a;
  --star:#f6efc4;
  --white:#fff;
}
*{box-sizing:border-box;margin:0;padding:0}
html,body{width:867px;height:1200px;overflow:hidden;background:var(--white)}
body{position:relative;font-family:"Cormorant Garamond",serif;color:var(--text)}
.abs{position:absolute}
.brand{left:103px;top:10px;font-size:11px;letter-spacing:-.3px;color:var(--ink);white-space:nowrap}
.main-nav{left:0;top:24px;width:867px;height:10px;font-size:5.4px;text-transform:uppercase;color:var(--ink)}
.main-nav span{position:absolute;top:0;white-space:nowrap}
.cart-icon{left:771px;top:6px}
.user-icon{left:814px;top:10px}
.product-photo{left:170px;top:50px;width:440px;height:355px;border-radius:6px;
  background:radial-gradient(ellipse at 50% 38%,#f2f2f2 0%,#e3dfcf 25%,#f6f6f6 55%,#fff 80%)}
.product-title{left:656px;top:53px;font-size:16px;line-height:22px;white-space:nowrap;font-weight:400;color:var(--ink)}
.section-label{font-size:22px;text-decoration:underline;text-underline-offset:4px;color:var(--ink)}
.price-label{left:656px;top:104px}
.price{left:657px;top:140px;font-size:15px;color:var(--ink)}
.desc-label{left:658px;top:160px}
.desc{left:657px;top:196px;width:110px;font-size:8.3px;line-height:10.2px}
.qty-label{left:656px;top:277px;font-size:8.3px}
.qty-box{left:656px;top:290px;width:22px;height:19px;background:#e6e6e6;font-size:8px;text-align:center;line-height:19px}
.buy-now{left:655px;top:324px;width:87px;height:35px;background:var(--accent);color:var(--white);font-size:17px;text-align:center;line-height:35px}
.bought-title{left:0;width:867px;top:403px;text-align:center;font-size:18px;color:var(--ink)}
.thumb{top:429px;width:108px;height:68px}
.reviews-title{left:0;width:840px;top:517px;text-align:center;font-size:26px;color:var(--ink)}
.review{left:109px;width:642px}
.review-head{position:relative;height:32px}
.avatar{position:absolute;left:0;top:0}
.reviewer{position:absolute;left:36px;top:6px;font-size:17px;color:var(--ink);white-space:nowrap}
.stars{position:absolute;left:134px;top:4px}
.review p{font-size:8.3px;line-height:10.4px;text-align:justify;margin-top:2px;color:var(--text)}
.map{left:110px;top:882px;width:274px;height:176px;background:linear-gradient(160deg,#7a7a7a,#5e5e5e)}
.contact{left:405px;top:882px;width:354px;height:170px;background:var(--panel);color:var(--white);font-family:"Lato",sans-serif}
.contact h2{position:absolute;left:24px;top:8px;font-weight:400;font-size:18.5px}
.contact .col{position:absolute;font-size:14.2px;line-height:17.6px}
.site-footer{left:0;top:1066px;width:867px;height:134px;
  background:linear-gradient(180deg,#000 0%,#0b0b0b 35%,#3c3c3c 55%,#121212 75%,#000 100%)}
.footer-brand{left:108px;top:1073px;color:var(--white);font-size:13px;display:flex;align-items:center;gap:4px}
.footer-brand i{display:block;width:9px;height:9px;background:var(--white)}
.socials{left:108px;top:1110px;display:flex;gap:14px}
.socials i{display:block;width:16px;height:16px;border-radius:50%;background:var(--white)}
.field{background:var(--white);color:var(--ink);font-family:"Lato",sans-serif;font-size:12.5px;padding:2px 4px;height:18px;line-height:15px}
.submit{left:685px;top:1173px;width:70px;height:24px;background:var(--accent);color:var(--white);font-family:"Lato",sans-serif;font-size:14px;text-align:center;line-height:24px}
</style>
</head>
<body>

<div class="abs brand">QUILLSTONE JEWELLERS</div>
<nav class="abs main-nav">
  <span style="left:222px">Engagement Rings</span>
  <span style="left:294px">Wedding Rings</span>
  <span style="left:355px">Diamond Earrings</span>
  <span style="left:427px">Diamond Pendants</span>
  <span style="left:501px">Loose Diamonds</span>
  <span style="left:567px">Sale Items</span>
  <span style="left:614px">Other Jewellery</span>
  <span style="left:681px">Education</span>
  <span style="left:731px">Wish List</span>
</nav>
<svg class="abs cart-icon" width="26" height="28" viewBox="0 0 26 28">
  <rect x="2" y="8" width="16" height="16" fill="none" stroke="#555" stroke-width="1"/>
  <path d="M6 8 V5 a4 4 0 0 1 8 0 V8" fill="none" stroke="#555" stroke-width="1"/>
  <circle cx="20" cy="5" r="4.5" fill="#e8212b"/>
  <text x="20" y="7" font-size="5" fill="#fff" text-anchor="middle" font-family="sans-serif">1</text>
</svg>
<svg class="abs user-icon" width="24" height="24" viewBox="0 0 24 24">
  <circle cx="12" cy="12" r="11.5" fill="#bbb"/>
  <circle cx="12" cy="9" r="4" fill="#fff"/>
  <path d="M4 19 a8 6 0 0 1 16 0" fill="#fff"/>
</svg>

<div class="abs product-photo" role="img" aria-label="Product photo: yellow gold solitaire ring with side diamonds"></div>

<h1 class="abs product-title">18K YELLOW<br>GOLD SERELLE</h1>
<div class="abs section-label price-label">Price</div>
<div class="abs price">$12,500</div>
<div class="abs section-label desc-label">Description</div>
<div class="abs desc">This beautiful 18k gold ring, comes with 12 side diamonds, weighing approximately 0.33 carats.<br>Custom made to fit your diamond.<br>Made to your desired ring size.</div>
<div class="abs qty-label">Quantity</div>
<div class="abs qty-box">1</div>
<div class="abs buy-now">Buy Now</div>

<div class="abs bought-title">Frequently Bought</div>
<div class="abs thumb" style="left:135px;background:linear-gradient(135deg,#d9a58a,#b07a9a)" role="img" aria-label="Purple gemstone halo ring"></div>
<div class="abs thumb" style="left:262px;background:linear-gradient(135deg,#fafafa,#cfcfcf)" role="img" aria-label="Diamond stud earrings"></div>
<div class="abs thumb" style="left:390px;background:linear-gradient(135deg,#8a8a8a,#4c4c4c)" role="img" aria-label="Patterned white gold band"></div>
<div class="abs thumb" style="left:517px;background:linear-gradient(135deg,#2a2a2a,#0d0d0d)" role="img" aria-label="Two diamond rings on dark display"></div>

<div class="abs reviews-title">Reviews</div>

<svg width="0" height="0" style="position:absolute">
  <defs>
    <symbol id="star" viewBox="0 0 20 20"><polygon points="10,0 12.9,6.6 20,7.3 14.6,12 16.2,19 10,15.3 3.8,19 5.4,12 0,7.3 7.1,6.6" fill="#f6efc4"/></symbol>
    <symbol id="person" viewBox="0 0 20 28"><circle cx="10" cy="7" r="6" fill="#111"/><path d="M1 28 V20 a9 8 0 0 1 18 0 V28 Z" fill="#111"/></symbol>
  </defs>
</svg>

<article class="abs review" style="top:549px">
  <div class="review-head">
    <svg class="avatar" width="20" height="28"><use href="#person"/></svg>
    <span class="reviewer">Ringseeker88</span>
    <svg class="stars" width="100" height="20"><use href="#star" x="0" width="20" height="20"/><use href="#star" x="20" width="20" height="20"/><use href="#star" x="40" width="20" height="20"/><use href="#star" x="60" width="20" height="20"/><use href="#star" x="80" width="20" height="20"/></svg>
  </div>
  <p>Lorem ipsum dolor sit amet, consectetur adipiscing elit, sed do eiusmod tempor incididunt ut labore et dolore magna aliqua. Ut enim ad minim veniam, quis nostrud exercitation ullamco laboris nisi ut aliquip ex ea commodo consequat. Duis aute irure dolor in reprehenderit in voluptate velit esse cillum dolore eu fugiat nulla pariatur. Excepteur sint occaecat cupidatat non proident, sunt in culpa qui officia deserunt mollit anim id est laborum. Sed ut perspiciatis unde omnis iste natus error sit voluptatem accusantium doloremque laudantium, totam rem aperiam, eaque ipsa quae ab illo inventore veritatis et quasi architecto beatae vitae dicta sunt explicabo. Nemo enim ipsam voluptatem quia voluptas sit aspernatur aut odit aut fugit, sed quia consequuntur magni dolores eos qui ratione voluptatem sequi nesciunt. Neque porro quisquam est, qui dolorem ipsum quia dolor sit amet, consectetur, adipisci velit, sed quia non numquam eius modi tempora incidunt ut labore et dolore magnam aliquam quaerat voluptatem.</p>
</article>

<article class="abs review" style="top:659px">
  <div class="review-head">
    <svg class="avatar" width="20" height="28"><use href="#person"/></svg>
    <span class="reviewer">Tmvrlk</span>
    <svg class="stars" width="100" height="20"><use href="#star" x="0" width="20" height="20"/><use href="#star" x="20" width="20" height="20"/><use href="#star" x="40" width="20" height="20"/><use href="#star" x="60" width="20" height="20"/><use href="#star" x="80" width="20" height="20"/></svg>
  </div>
  <p>Lorem ipsum dolor sit amet, consectetur adipiscing elit, sed do eiusmod tempor incididunt ut labore et dolore magna aliqua. Ut enim ad minim veniam, quis nostrud exercitation ullamco laboris nisi ut aliquip ex ea commodo consequat. Duis aute irure dolor in reprehenderit in voluptate velit esse cillum dolore eu fugiat nulla pariatur. Excepteur sint occaecat cupidatat non proident, sunt in culpa qui officia deserunt mollit anim id est laborum. Sed ut perspiciatis unde omnis iste natus error sit voluptatem accusantium doloremque laudantium, totam rem aperiam, eaque ipsa quae ab illo inventore veritatis et quasi architecto beatae vitae dicta sunt explicabo. Nemo enim ipsam voluptatem quia voluptas sit aspernatur aut odit aut fugit, sed quia consequuntur magni dolores eos qui ratione voluptatem sequi nesciunt. Neque porro quisquam est, qui dolorem ipsum quia dolor sit amet, consectetur, adipisci velit, sed quia non numquam eius modi tempora incidunt ut labore et dolore magnam aliquam quaerat voluptatem.</p>
</article>

<article class="abs review" style="top:771px">
  <div class="review-head">
    <svg class="avatar" width="20" height="28"><use href="#person"/></svg>
    <span class="reviewer">Dsparrow</span>
    <svg class="stars" width="100" height="20"><use href="#star" x="0" width="20" height="20"/><use href="#star" x="20" width="20" height="20"/><use href="#star" x="40" width="20" height="20"/><svg x="60" width="12" height="20"><use href="#star" width="20" height="20"/></svg></svg>
  </div>
  <p>Lorem ipsum dolor sit amet, consectetur adipiscing elit, sed do eiusmod tempor incididunt ut labore et dolore magna aliqua. Ut enim ad minim veniam, quis nostrud exercitation ullamco laboris nisi ut aliquip ex ea commodo consequat. Duis aute irure dolor in reprehenderit in voluptate velit esse cillum dolore eu fugiat nulla pariatur. Excepteur sint occaecat cupidatat non proident, sunt in culpa qui officia deserunt mollit anim id est laborum. Sed ut perspiciatis unde omnis iste natus error sit voluptatem accusantium doloremque laudantium, totam rem aperiam, eaque ipsa quae ab illo inventore veritatis et quasi architecto beatae vitae dicta sunt explicabo. Nemo enim ipsam voluptatem quia voluptas sit aspernatur aut odit aut fugit, sed quia consequuntur magni dolores eos qui ratione voluptatem sequi nesciunt. Neque porro quisquam est, qui dolorem ipsum quia dolor sit amet, consectetur, adipisci velit, sed quia non numquam eius modi tempora incidunt ut labore et dolore magnam aliquam quaerat voluptatem.</p>
</article>

<div class="abs map" role="img" aria-label="Map showing the store location"></div>

<section class="abs contact">
  <h2>Contact Information</h2>
  <div class="col" style="left:7px;top:42px">Phone:<br>(555) 014 – 2290</div>
  <div class="col" style="left:10px;top:82px">Fax:<br>(555) 014 – 2291</div>
  <div class="col" style="left:16px;top:128px">E-mail:<br>Sales@quillstone.example</div>
  <div class="col" style="left:176px;top:44px">Address:<br>(Courier Only)<br>Quillstone Jewellers<br>41 Harlow Lane<br>Brackenfield, 00417</div>
</section>

<footer class="abs site-footer" role="img" aria-label="Scattered loose diamonds on a dark reflective surface"></footer>
<div class="abs footer-brand"><i></i>QUILLSTONE</div>
<div class="abs socials"><i></i><i></i><i></i></div>
<div class="abs field" style="left:518px;top:1070px;width:113px">Name:</div>
<div class="abs field" style="left:645px;top:1070px;width:113px">Phone:</div>
<div class="abs field" style="left:517px;top:1096px;width:242px">Email</div>
<div class="abs field" style="left:518px;top:1119px;width:240px;height:55px">Message:</div>
<div class="abs submit">Submit</div>

</body>
</html>
```